Postcard for Antique Furniture Restorer

My business is to restore antique furniture. I am based in Sydney, Australia.

I will be using this postcard to promote my business.
I will give it to customers like a With Compliments card.

Sometimes I will be writing information on the back of the card.

Design for Postcard Size eg 148 X 105mm

Front of card:

Attached are images of Antique furniture - please use ONLY 1 of the 3 images.
Deep etch the image on a white or cream background.

On front of card add these words:
Timber Reborn
antique furniture restoration

Antiques travel through time, seeing generations of families
Through time they remain - they tell a continuing story
Be part of the journey

Back of postcard:
(leave space for notes to be handwritten)

Add these words:

Timber Reborn
Corin Maddox
mobile 0437 552 618
www.oakandvarnishcraft.com.au

Industry/Entity Type

Business

Font styles to use
Serif
Sans Serif

Colors
fefdec
ffffff

Requirements
Must have
• Use only 1 image. Image must be deep etched.

```html
<!DOCTYPE html>
<html lang="en">
<head>
<meta charset="utf-8">
<title>Timber Reborn – Postcard Front and Back</title>
<link rel="stylesheet" href="https://fonts.googleapis.com/css2?family=Libre+Baskerville:wght@400;700&family=Lato:wght@400;700&family=Courier+Prime:wght@400;700&display=swap">
<style>
  :root {
    --backdrop: #ececec;
    --parchment-light: #f3ead6;
    --parchment-mid: #e6d3ac;
    --parchment-edge: #c9a66b;
    --parchment-back-light: #f6f0e2;
    --parchment-back-edge: #e2d2b2;
    --ink: #2a2418;
    --ink-soft: #3a3224;
    --frame-ink: #2d2a24;
    --timber-dark: #4a2a18;
    --timber-mid: #6e4424;
    --timber-light: #8c6236;
  }
  * { margin: 0; padding: 0; box-sizing: border-box; }
  html, body {
    width: 1200px; height: 900px; overflow: hidden;
    background: var(--backdrop);
  }
  .canvas { position: relative; width: 1200px; height: 900px; }

  .card {
    position: absolute; top: 138px;
    width: 492px; height: 692px;
    box-shadow: 0 6px 18px rgba(0,0,0,0.18);
    overflow: hidden;
  }
  .card--front {
    left: 96px;
    background:
      radial-gradient(ellipse 60% 55% at 50% 48%, var(--parchment-light) 0%, var(--parchment-mid) 70%, var(--parchment-edge) 115%);
  }
  .card--back {
    left: 639px;
    background:
      radial-gradient(ellipse 70% 65% at 50% 40%, var(--parchment-back-light) 0%, #efe5cf 70%, var(--parchment-back-edge) 120%);
  }

  .frame { position: absolute; left: 0; top: 0; }

  .feature-piece {
    position: absolute; left: 116px; top: 202px;
    width: 270px; height: 190px;
    border-radius: 14px;
    background: radial-gradient(ellipse 70% 65% at 50% 45%, var(--timber-light) 0%, var(--timber-mid) 55%, var(--timber-dark) 100%);
  }

  .front-text { position: absolute; left: 0; width: 100%; text-align: center; color: var(--ink); }
  .brand-title {
    top: 532px;
    font-family: "Libre Baskerville", Georgia, serif;
    font-size: 21px; font-weight: 400; letter-spacing: 2.5px;
  }
  .title-rule { position: absolute; left: 171px; top: 562px; }
  .brand-tagline {
    top: 578px;
    font-family: "Lato", Arial, sans-serif;
    font-size: 9.5px; font-weight: 700; letter-spacing: 1px;
  }
  .brand-story {
    top: 603px;
    font-family: "Libre Baskerville", Georgia, serif;
    font-size: 10.5px; line-height: 17.5px; color: var(--ink-soft);
  }

  .contact {
    position: absolute; left: 22px; top: 592px;
    font-family: "Courier Prime", "Courier New", monospace;
    font-size: 13.5px; line-height: 17px; color: var(--ink);
  }
  .contact__name, .contact__label { font-weight: 700; }
  .contact__business { margin-top: 17px; }
</style>
</head>
<body>
<main class="canvas">
  <section class="card card--front" aria-label="Postcard front">
    <svg class="frame" width="492" height="692" viewBox="0 0 492 692" aria-hidden="true">
      <ellipse cx="247" cy="257" rx="182" ry="238" fill="none" stroke="var(--frame-ink)" stroke-width="2"/>
      <ellipse cx="247" cy="257" rx="172" ry="228" fill="none" stroke="var(--frame-ink)" stroke-width="2.5"/>
      <ellipse cx="247" cy="257" rx="166" ry="222" fill="var(--parchment-light)" fill-opacity="0.45" stroke="var(--frame-ink)" stroke-width="1.2"/>
    </svg>
    <div class="feature-piece" role="img" aria-label="Deep-etched photograph of a restored antique round pedestal table in dark polished timber"></div>

    <h1 class="front-text brand-title">TIMBER REBORN</h1>
    <svg class="title-rule" width="150" height="10" viewBox="0 0 150 10" aria-hidden="true">
      <path d="M2 6 Q40 1 75 5 T148 4" fill="none" stroke="var(--ink)" stroke-width="1.2"/>
    </svg>
    <p class="front-text brand-tagline">ANTIQUE FURNITURE RESTORATION</p>
    <p class="front-text brand-story">
      Antiques travel through time, seeing generations of families.<br>
      Through time they remain - they tell a continuing story.<br>
      Be part of the journey.
    </p>
  </section>

  <section class="card card--back" aria-label="Postcard back">
    <div class="contact">
      <p class="contact__name">Corin Maddox</p>
      <p><span class="contact__label">m_</span>0437 552 618</p>
      <p class="contact__business">timber reborn - antique furniture restoration</p>
      <p>www.oakandvarnishcraft.com.au</p>
    </div>
  </section>
</main>
</body>
</html>
```